Web design - holistic filmmaker

I need a design for my new website.

I am a holistic filmmaker, ie I make films for healers, alternative practitioners, spiritual people and institutions that offer training in this field.

The design should be noble, bright, convey the feeling of space and expanse and have some particularly beautiful color accents.

The structure is: start page, offer, references, about me, imprint.

As an idea for the start page, I thought that either I could introduce myself as a filmmaker and my offer, or we could start right on the start page with the references, ie photos and links to already realized projects.

If you want more information or an exchange, I'd love to hear from you. At the moment I just don't know how to describe it better.

The winner will then be asked to design a logo.

Target Market(s)

healers, alternative practitioners, spiritual people and institutions that offer training in this field

Industry/Entity Type

Film production

Number of Pages Required

3 page

```html
<!DOCTYPE html>
<html lang="en">
<head>
<meta charset="utf-8">
<title>Marlo – Holistic Filmmaker</title>
<link href="https://fonts.googleapis.com/css2?family=Poppins:wght@300;400;500;600;700&family=Lato:wght@400;700&display=swap" rel="stylesheet">
<style>
:root{
  --orange:#f15a22;
  --tan:#bf9584;
  --tan-dark:#b08a70;
  --sand:#f8f3ee;
  --sand-deep:#f3ebe2;
  --ink:#4a4a4a;
  --dark:#1d1d1d;
  --white:#ffffff;
}
*{margin:0;padding:0;box-sizing:border-box}
html,body{width:1200px;height:3271px;overflow:hidden;background:var(--white)}
body{position:relative;font-family:"Poppins",sans-serif;color:var(--ink)}
.abs{position:absolute}

/* hero */
.hero-photo{left:0;top:0;width:1200px;height:640px;
  background:radial-gradient(ellipse at 70% 30%,#e7a15a 0%,#c0632a 35%,#6a3218 70%,#2b1710 100%)}
.hero-shade{left:0;top:0;width:1200px;height:640px;
  background:linear-gradient(180deg,rgba(0,0,0,.25) 0%,rgba(0,0,0,0) 25%,rgba(0,0,0,0) 60%,rgba(60,20,5,.35) 100%)}
.hero-wave{left:0;top:520px}
.brand{display:flex;align-items:center;gap:10px}
.brand-mark{width:56px;height:52px;border:3px solid var(--orange);border-radius:6px;background:rgba(241,90,34,.12)}
.brand-name{font-weight:700;font-size:48px;line-height:1;letter-spacing:1px}
.brand-sub{font-size:12px;color:var(--orange);letter-spacing:1px;margin-top:2px}
.hero .brand-name{color:var(--white)}
.nav{top:48px;left:588px;display:flex;font-size:15px;letter-spacing:2.4px;color:var(--white);font-weight:500}
.nav span{position:absolute;white-space:nowrap}
.nav .active{color:var(--orange)}
.hero-title{left:377px;top:304px;font-size:82px;font-weight:700;line-height:88px;color:var(--white);letter-spacing:-1.5px;white-space:nowrap}
.hero-title .accent{color:var(--orange)}
.hero-sub{left:377px;top:490px;font-size:27px;line-height:32px;color:var(--orange);font-weight:400;white-space:nowrap}

/* sections */
.heading{left:0;width:1200px;text-align:center;color:var(--tan);font-size:33px;font-weight:400}
.divider{left:406px;width:392px;height:44px}
.divider .line{position:absolute;top:22px;width:162px;border-top:1px dotted #d2b6a4}
.divider .line.l{left:0}.divider .line.r{right:0}
.divider .ornament{position:absolute;left:175px;top:0;width:42px;height:42px;border-radius:50%;
  background:radial-gradient(circle,#e9cfae 0%,#dcb78f 70%,#f1e2cf 100%)}
.band{left:0;width:1200px;background:var(--sand)}
.copy{left:0;width:1200px;text-align:center;font-size:17.5px;font-weight:300;line-height:26px;color:#555}
.btn{width:164px;height:34px;background:var(--tan-dark);color:var(--white);font-size:22px;font-weight:300;text-align:center;line-height:34px}
.decor{border-radius:50%;background:radial-gradient(circle,rgba(226,200,170,.18) 0%,rgba(226,200,170,.12) 55%,rgba(255,255,255,0) 72%)}

/* videos */
.thumb{width:258px;height:183px}
.thumb.a{background:linear-gradient(160deg,#3d6fa3 0%,#8fb0cf 45%,#c9cfd4 100%)}
.thumb.b{background:linear-gradient(135deg,#2b2a26 0%,#6b6556 40%,#a58a6c 70%,#4c3b2c 100%)}
.thumb.c{background:linear-gradient(120deg,#5a4b40 0%,#d9d2cb 35%,#efe9e6 60%,#c27aa4 100%)}
.play{width:74px;height:52px;background:var(--white);border-radius:14px}
.play svg{position:absolute;left:28px;top:16px}
.card{width:192px;height:151px;background:var(--orange);color:var(--white)}
.card h3{position:absolute;top:34px;left:0;width:192px;text-align:center;font-size:24px;font-weight:400}
.card p{position:absolute;top:90px;left:10px;width:180px;font-size:13px;line-height:13px;font-weight:400}

/* clients */
.client{width:153px;height:124px;background:var(--white);display:flex;align-items:center;justify-content:center;gap:8px;font-size:19px;color:#8a5a4a;font-weight:400}
.client .dot{width:14px;height:14px;border-radius:50%;background:var(--orange)}

/* footer */
.footer-bg{left:0;top:2826px;width:1200px;height:445px}
.foot-brand .brand-name{color:var(--dark)}
.foot-text{font-family:"Lato",sans-serif;font-size:17px;color:#222;line-height:27px}
.foot-label{font-size:18px;color:var(--orange);font-weight:300}
.contact{font-family:"Lato",sans-serif;font-size:16px;color:#222;display:flex;align-items:center;gap:10px}
.news-thumb{width:85px;height:86px}
.news-title{font-size:13px;font-weight:600;color:#6b5a52}
.news-meta{font-size:13px;font-style:italic;color:var(--orange);font-weight:300}
.gal{width:76px;height:76px}
.copyright{left:0;top:3228px;width:1200px;text-align:center;font-family:"Lato",sans-serif;font-size:12px;color:#222}
.follow{top:3226px;left:951px;display:flex;align-items:center;gap:7px;font-size:12px}
.follow .label{color:var(--orange)}
.follow .net{font-family:"Lato",sans-serif;font-size:12px;color:#111;font-weight:700}
</style>
</head>
<body>

<header class="hero">
  <div class="abs hero-photo" role="img" aria-label="Photo of the filmmaker holding a film camera in a warm, golden street scene"></div>
  <div class="abs hero-shade"></div>
  <svg class="abs hero-wave" width="1200" height="120" viewBox="0 0 1200 120">
    <path d="M0,90 C220,20 520,40 760,65 C950,85 1100,60 1200,45 L1200,120 L0,120 Z" fill="#ffffff"/>
  </svg>
  <div class="abs brand" style="left:28px;top:24px">
    <div class="brand-mark"></div>
    <div><div class="brand-name">MARLO</div><div class="brand-sub">Holistic Filmmaker</div></div>
  </div>
  <nav class="abs nav">
    <span class="active" style="left:0">HOME</span>
    <span style="left:93px">OFFER</span>
    <span style="left:188px">REFERENCES</span>
    <span style="left:339px">ABOUT ME</span>
    <span style="left:474px">IMPRINT</span>
  </nav>
  <h1 class="abs hero-title">My name is <span class="accent">MARLO</span><br>and I do movies</h1>
  <p class="abs hero-sub">with enthusiasm and wholeheartedly.<br>I am a holistic filmmaker.</p>
  <svg class="abs" style="left:660px;top:565px" width="540" height="50" viewBox="0 0 540 50">
    <line x1="37" y1="13" x2="508" y2="13" stroke="#f15a22" stroke-width="1.5"/>
    <circle cx="37" cy="13" r="6" fill="#f15a22"/>
    <line x1="13" y1="38" x2="440" y2="38" stroke="#cfcfcf" stroke-width="1"/>
    <circle cx="13" cy="38" r="6" fill="#ffffff" stroke="#cccccc"/>
  </svg>
</header>

<div class="abs decor" style="left:850px;top:600px;width:420px;height:670px" role="img" aria-label="Faint flower decoration"></div>

<section>
  <h2 class="abs heading" style="top:690px">Holistic Filmmaker Solutions</h2>
  <div class="abs divider" style="top:748px"><span class="line l"></span><span class="ornament" role="img" aria-label="Small flower ornament"></span><span class="line r"></span></div>
  <div class="abs heading" style="top:797px;font-size:22px;font-weight:300">About Me</div>
  <div class="abs band" style="top:830px;height:266px;background:rgba(248,243,238,.85)"></div>
  <p class="abs copy" style="top:866px">Mein Name ist Marlo und ich mache Filme - mit Begeisterung und von ganzem Herzen. Ich bin ein holistischer Filmemacher.</p>
  <p class="abs copy" style="top:919px">Ende der 1990er Jahre stand ich vor der Frage, ob ich beruflich in die Alternativmedizin oder in die Filmbranche gehen solle.<br>Beruflich habe ich mich damals für den Film entschieden, aber das Geistig-Spirituelle und meine Leidenschaft für die<br>sogenannten alternativen Heilmethoden begleiten mich seitdem fast genauso intensiv.</p>
  <div class="abs btn" style="left:504px;top:1015px">Know More</div>
</section>

<section>
  <h2 class="abs heading" style="top:1138px">My Latest Videos</h2>
  <div class="abs divider" style="top:1196px"><span class="line l"></span><span class="ornament" role="img" aria-label="Small flower ornament"></span><span class="line r"></span></div>

  <div class="abs thumb a" style="left:71px;top:1251px" role="img" aria-label="Video still of a woman in front of a city tower"></div>
  <div class="abs thumb b" style="left:471px;top:1251px" role="img" aria-label="Video still of two people in conversation"></div>
  <div class="abs thumb c" style="left:853px;top:1251px" role="img" aria-label="Video still of a woman in a bright room"></div>
  <div class="abs card" style="left:104px;top:1358px"><h3>Tao Kelin</h3><p>Lorem ipsum is simply dummy text of the printing and typesetting industry.</p></div>
  <div class="abs card" style="left:508px;top:1358px"><h3>Orvanta</h3><p>Lorem ipsum is simply dummy text of the printing and typesetting industry.</p></div>
  <div class="abs card" style="left:886px;top:1358px"><h3>Orvanta</h3><p>Lorem ipsum is simply dummy text of the printing and typesetting industry.</p></div>
  <div class="abs play" style="left:160px;top:1315px"><svg width="18" height="20"><path d="M0,0 L18,10 L0,20 Z" fill="#333"/></svg></div>
  <div class="abs play" style="left:566px;top:1315px"><svg width="18" height="20"><path d="M0,0 L18,10 L0,20 Z" fill="#333"/></svg></div>
  <div class="abs play" style="left:944px;top:1315px"><svg width="18" height="20"><path d="M0,0 L18,10 L0,20 Z" fill="#333"/></svg></div>

  <div class="abs thumb a" style="left:71px;top:1567px" role="img" aria-label="Video still of a woman in front of a city tower"></div>
  <div class="abs thumb b" style="left:471px;top:1567px" role="img" aria-label="Video still of two people in conversation"></div>
  <div class="abs thumb c" style="left:853px;top:1567px" role="img" aria-label="Video still of a woman in a bright room"></div>
  <div class="abs card" style="left:104px;top:1674px"><h3>Tao Kelin</h3><p>Lorem ipsum is simply dummy text of the printing and typesetting industry.</p></div>
  <div class="abs card" style="left:508px;top:1674px"><h3>Orvanta</h3><p>Lorem ipsum is simply dummy text of the printing and typesetting industry.</p></div>
  <div class="abs card" style="left:886px;top:1674px"><h3>Orvanta</h3><p>Lorem ipsum is simply dummy text of the printing and typesetting industry.</p></div>
  <div class="abs play" style="left:160px;top:1631px"><svg width="18" height="20"><path d="M0,0 L18,10 L0,20 Z" fill="#333"/></svg></div>
  <div class="abs play" style="left:566px;top:1631px"><svg width="18" height="20"><path d="M0,0 L18,10 L0,20 Z" fill="#333"/></svg></div>
  <div class="abs play" style="left:944px;top:1631px"><svg width="18" height="20"><path d="M0,0 L18,10 L0,20 Z" fill="#333"/></svg></div>
</section>

<section>
  <div class="abs band" style="top:2007px;height:266px"></div>
  <div class="abs decor" style="left:-180px;top:1840px;width:440px;height:600px" role="img" aria-label="Faint flower decoration"></div>
  <h2 class="abs heading" style="top:1910px">Making a movie is always a journey to yourself</h2>
  <div class="abs divider" style="top:1960px"><span class="line l"></span><span class="ornament" role="img" aria-label="Small flower ornament"></span><span class="line r"></span></div>
  <p class="abs copy" style="top:2042px">Films for Clear Minds is aimed at all people and institutions whose striving for<br>truthfulness is the driving force behind their actions.</p>
  <p class="abs copy" style="top:2122px">I accompany you on the way to portraying your essence.means and without special effects,</p>
  <div class="abs btn" style="left:504px;top:2192px">Know More</div>
</section>

<section>
  <h2 class="abs heading" style="top:2384px">My Clients</h2>
  <div class="abs divider" style="top:2436px"><span class="line l"></span><span class="ornament" role="img" aria-label="Small flower ornament"></span><span class="line r"></span></div>
  <div class="abs band" style="top:2480px;height:267px"></div>
  <div class="abs client" style="left:156px;top:2553px">Lina Vey</div>
  <div class="abs client" style="left:337px;top:2553px"><span class="dot"></span>Orvanta</div>
  <div class="abs client" style="left:517px;top:2553px"><span class="dot"></span>Tao Kelin</div>
  <div class="abs client" style="left:697px;top:2553px;font-size:17px">Halden Spiele</div>
  <div class="abs client" style="left:879px;top:2553px">Marlo</div>
</section>

<footer>
  <svg class="abs footer-bg" width="1200" height="445" viewBox="0 0 1200 445">
    <path d="M0,50 C250,10 500,0 700,5 C900,10 1080,40 1200,75 L1200,445 L0,445 Z" fill="#f8f3ee"/>
  </svg>
  <div class="abs brand foot-brand" style="left:41px;top:2892px">
    <div class="brand-mark"></div>
    <div><div class="brand-name">MARLO</div><div class="brand-sub">Holistic Filmmaker</div></div>
  </div>
  <p class="abs foot-text" style="left:47px;top:2968px">Lorem ipsum dolor sit amet, consectetur<br>adipisicing elit, sed do eiusmod.</p>
  <div class="abs foot-label" style="left:47px;top:3040px">Address</div>
  <div class="abs contact" style="left:47px;top:3074px"><svg width="16" height="16" viewBox="0 0 16 16"><path d="M3,1 L6,1 L7,5 L5,6 C6,8.5 7.5,10 10,11 L11,9 L15,10 L15,13 C15,14 14,15 13,15 C6,14 2,10 1,3 C1,2 2,1 3,1 Z" fill="#111"/></svg>48 Linden Row, Harbor Town, HT 20417</div>
  <div class="abs contact" style="left:47px;top:3100px"><svg width="16" height="16" viewBox="0 0 16 16"><path d="M8,1 L15,7 L1,7 Z M1,9 L15,9 L15,15 L1,15 Z" fill="#111"/></svg>Email: hello@marlofilm.example</div>
  <div class="abs contact" style="left:47px;top:3126px"><svg width="16" height="16" viewBox="0 0 16 16"><rect x="1" y="3" width="14" height="11" fill="#111"/><path d="M1,3 L8,9 L15,3" stroke="#fff" stroke-width="1.4" fill="none"/></svg>Telephone: +1(800)555-0142</div>

  <div class="abs foot-label" style="left:447px;top:2936px">Latest News</div>
  <div class="abs news-thumb" style="left:448px;top:2990px;background:linear-gradient(135deg,#e8d9c0,#c98f4a 55%,#8a6a3a)" role="img" aria-label="Photo of fresh fruit and vegetables"></div>
  <div class="abs news-title" style="left:555px;top:2992px">The Light of Live Foods</div>
  <div class="abs news-meta" style="left:555px;top:3023px">Nora Feld . August 22, 2016</div>
  <div class="abs news-thumb" style="left:448px;top:3095px;background:radial-gradient(circle,#8bbf3a,#3f7a1e 70%,#2a4a18)" role="img" aria-label="Photo of a green smoothie"></div>
  <div class="abs news-title" style="left:555px;top:3097px">The Light of Live Foods</div>
  <div class="abs news-meta" style="left:555px;top:3128px">Nora Feld . August 22, 2016</div>

  <div class="abs foot-label" style="left:831px;top:2940px">Our Video Gallery</div>
  <div class="abs gal" style="left:829px;top:2990px;background:linear-gradient(135deg,#dcdcdc,#555)" role="img" aria-label="Gallery still, black and white portrait"></div>
  <div class="abs gal" style="left:911px;top:2990px;background:linear-gradient(135deg,#c9583a,#6b2a1c)" role="img" aria-label="Gallery still, filming on location"></div>
  <div class="abs gal" style="left:993px;top:2990px;background:linear-gradient(135deg,#cfcfcf,#4a4a4a)" role="img" aria-label="Gallery still, black and white portrait"></div>
  <div class="abs gal" style="left:1075px;top:2990px;background:linear-gradient(135deg,#d89a4a,#5e3a1e)" role="img" aria-label="Gallery still, warm street scene"></div>
  <div class="abs gal" style="left:829px;top:3072px;background:linear-gradient(135deg,#b84a36,#3a1e1a)" role="img" aria-label="Gallery still, filming on location"></div>
  <div class="abs gal" style="left:911px;top:3072px;background:linear-gradient(135deg,#9bb7cf,#4f6a80)" role="img" aria-label="Gallery still, outdoor portrait"></div>
  <div class="abs gal" style="left:993px;top:3072px;background:linear-gradient(135deg,#e0b060,#7a4a24)" role="img" aria-label="Gallery still, warm interior"></div>
  <div class="abs gal" style="left:1075px;top:3072px;background:linear-gradient(135deg,#c8a878,#5a4a3a)" role="img" aria-label="Gallery still, outdoor portrait"></div>

  <div class="abs copyright">MARLO FILM © 2023 All Rights Reserved</div>
  <div class="abs follow"><span class="label">Follow up</span><span class="net">Kiro</span><span class="net">Lumo</span><span class="net">Pipa</span><span class="net">Vidu</span><span class="net">Nexo</span></div>
</footer>

</body>
</html>
```